The Quillfern Espresso Nook Coffee Card

would like a coffee card designed for our café. Most cards are so boring and I need to stand out from the crowd (The Quillfern ). I require our logo on one side or the business name also a place for people to write their name and mobile number (collecting data base) and on the back the following
customer gets a stamp for the 1st three coffees purchased, on the 3rd one they get a free upsize. another 2 stamps and on the 3rd one (6) gets a free coffee, another 2 stamps and the customer gets another upsize (9th coffee purchased) and on the 10th card they recivie a voucher for a free pizza.
small print | one free pizza for dinner dining (not available for takeaways and must book), Cant be used with any other offers, opts in to hear from the herd if there is a deal on. cant trade for cash or gift

```html
<!DOCTYPE html>
<html lang="en">
<head>
<meta charset="utf-8">
<title>The Quillfern Espresso Nook – Coffee Card</title>
<link rel="stylesheet" href="https://fonts.googleapis.com/css2?family=Oswald:wght@600&family=Open+Sans:wght@400&family=Arimo:wght@400&display=swap">
<style>
  :root {
    --backdrop: #e9e6e1;
    --card: #f5f1e8;
    --grain: #ece3d3;
    --ink: #1c1a18;
    --ink-soft: #2d2a27;
    --rule: #8a8580;
    --shadow: rgba(0, 0, 0, 0.18);
  }
  * { box-sizing: border-box; margin: 0; padding: 0; }
  html, body {
    width: 1200px;
    height: 900px;
    overflow: hidden;
    background: var(--backdrop);
  }
  .canvas {
    width: 1200px;
    height: 900px;
    display: flex;
    flex-direction: column;
    align-items: center;
    justify-content: center;
    gap: 48px;
  }
  .card {
    position: relative;
    width: 700px;
    height: 400px;
    background: var(--card);
    box-shadow: 0 8px 24px var(--shadow);
    overflow: hidden;
  }

  /* Front */
  .card-front__texture {
    position: absolute;
    inset: 0;
    background: linear-gradient(180deg, var(--card) 0%, var(--grain) 50%, var(--card) 100%);
  }
  .brand {
    position: absolute;
    top: 52px;
    left: 0;
    right: 0;
    display: flex;
    flex-direction: column;
    align-items: center;
  }
  .brand__dot {
    width: 44px;
    height: 44px;
    border-radius: 50%;
    background: var(--ink);
    margin-bottom: 14px;
  }
  .brand__name {
    font-family: "Oswald", sans-serif;
    font-weight: 600;
    color: var(--ink);
    font-size: 34px;
    letter-spacing: 0.5px;
    text-transform: uppercase;
    line-height: 1;
    padding-bottom: 6px;
    border-bottom: 1.5px solid var(--ink);
  }
  .brand__tagline {
    font-family: "Oswald", sans-serif;
    font-weight: 600;
    color: var(--ink);
    font-size: 11px;
    letter-spacing: 1.5px;
    text-transform: uppercase;
    margin-top: 6px;
  }
  .contact-form {
    position: absolute;
    left: 72px;
    right: 72px;
    top: 228px;
    font-family: "Open Sans", sans-serif;
    color: var(--ink);
    font-size: 21px;
  }
  .contact-form__row {
    display: flex;
    align-items: flex-end;
    margin-bottom: 26px;
  }
  .contact-form__label { margin-right: 6px; line-height: 1; }
  .contact-form__line {
    flex: 1;
    border-bottom: 1.5px solid var(--ink-soft);
    height: 1px;
  }

  /* Back */
  .card-back__mark {
    position: absolute;
    top: 30px;
    left: 50%;
    width: 40px;
    height: 40px;
    margin-left: -20px;
    border-radius: 50%;
    background: var(--ink);
  }
  .rewards {
    position: absolute;
    top: 92px;
    left: 66px;
    right: 66px;
    font-family: "Arimo", sans-serif;
    color: var(--ink-soft);
    font-size: 19px;
    line-height: 1.2;
    text-align: center;
  }
  .divider {
    position: absolute;
    left: 50%;
    width: 200px;
    margin-left: -100px;
    border-top: 1px solid var(--rule);
  }
  .divider--top { top: 244px; }
  .divider--bottom { top: 306px; }
  .small-print {
    position: absolute;
    top: 258px;
    left: 60px;
    right: 60px;
    font-family: "Arimo", sans-serif;
    color: var(--ink);
    font-size: 11.5px;
    line-height: 1.35;
    text-align: center;
  }
  .card-back__band {
    position: absolute;
    left: 0;
    right: 0;
    bottom: 0;
    height: 34px;
    background: var(--ink);
  }
</style>
</head>
<body>
<main class="canvas">

  <section class="card card-front" aria-label="Coffee card front">
    <div class="card-front__texture" role="img" aria-label="Light wood-grain stripe texture across the card"></div>
    <div class="brand">
      <span class="brand__dot"></span>
      <span class="brand__name">The Quillfern</span>
      <span class="brand__tagline">Espresso Nook</span>
    </div>
    <div class="contact-form">
      <div class="contact-form__row">
        <span class="contact-form__label">Name</span>
        <span class="contact-form__line"></span>
      </div>
      <div class="contact-form__row">
        <span class="contact-form__label">Mobile</span>
        <span class="contact-form__line"></span>
      </div>
    </div>
  </section>

  <section class="card card-back" aria-label="Coffee card back">
    <span class="card-back__mark"></span>
    <p class="rewards">Customer gets a stamp for the 1st three coffees purchased, on the 3rd one they get a free upsize. another 2 stamps and on the 3rd one (6) gets a free coffee, another 2 stamps and the customer gets another upsize (9th coffee purchased) and on the 10th card they recivie a voucher for a free pizza.</p>
    <span class="divider divider--top"></span>
    <p class="small-print">one free pizza for dinner dining (not available for takeaways and must book), Cant be used with any other offers, opts in to hear from the herd if there is a deal on. cant trade for cash or gift</p>
    <span class="divider divider--bottom"></span>
    <div class="card-back__band"></div>
  </section>

</main>
</body>
</html>
```